The Brightpath Scholar, an online college fair for non-traditional students, needs a web site

I need design and coding for a functioning web site that will serve as an online college fair that connects non-traditional students with college admissions officers and college advisors. I have chosen Wordpress and the "Meridian" theme for the site, and you can see what I already have here: https://brightpathscholar.example/
I need help setting up the site's pages and functionality, including SEO optimization and a password protected area. I will manage all content. In addition to me as the administrator, other users will be: college admissions officers, non-traditional students (like homeschoolers), and college advisors.
Target Market(s)
Homeschoolers and college/university admissions officers
Industry/Entity Type
College
Coding
Coded - Design and coding required
Number of Pages Required
5+ page
Requirements
Must have
- - An inviting but professional look (see the logo as a starting point)
- - Easy to navigate
- - A way to register subscribed members (students)
- - A password-protected "members only" area
- - Virtual "booths" on the Schools page that lead to a detail page for each school
- - SEO optimized
Nice to have
- - Searchable site

```html
<!DOCTYPE html>
<html lang="en">
<head>
<meta charset="utf-8">
<title>The Brightpath Scholar</title>
<link href="https://fonts.googleapis.com/css2?family=Roboto:wght@400;500;700&family=Roboto+Condensed:wght@700&display=swap" rel="stylesheet">
<style>
:root{
  --red:#b3121b;
  --red-dark:#8a0c13;
  --ink:#2b2b2b;
  --muted:#777;
  --line:#e3e3e3;
  --paper:#ffffff;
  --mist:#f1f1f1;
  --footer:#2a2a2a;
  --footer-deep:#1b1b1b;
}
*{box-sizing:border-box;margin:0;padding:0}
html,body{width:1200px;height:3852px;overflow:hidden}
body{font-family:"Roboto",Arial,sans-serif;color:var(--ink);background:var(--paper);position:relative;font-size:13px;line-height:1.55}
.heading{font-family:"Roboto Condensed","Arial Narrow",sans-serif;font-weight:700;text-transform:uppercase;letter-spacing:.5px}
.block{position:absolute;left:0;width:1200px}
.photo{position:absolute}
.btn{display:inline-block;background:var(--red);color:#fff;font-weight:700;font-size:12px;text-transform:uppercase;padding:10px 24px;border-radius:3px;white-space:nowrap}

/* header */
.site-header{top:0;height:100px;background:var(--paper);box-shadow:0 2px 6px rgba(0,0,0,.08);z-index:3}
.brand{position:absolute;left:40px;top:30px;display:flex;align-items:center;gap:10px}
.brand-mark{width:40px;height:40px;background:var(--red)}
.brand-name{font-family:"Roboto Condensed",sans-serif;font-weight:700;font-size:24px;color:var(--red);text-transform:uppercase;white-space:nowrap}
.contact-strip{position:absolute;right:40px;top:14px;font-size:11px;color:var(--muted)}
.contact-strip b{color:var(--red)}
.main-nav{position:absolute;right:224px;top:58px;display:flex;gap:20px;font-size:12px;font-weight:700;text-transform:uppercase;white-space:nowrap}
.main-nav a:first-child{color:var(--red)}
.login{position:absolute;right:40px;top:50px;padding:8px 16px}

/* hero */
.hero{top:100px;height:600px}
.hero .photo{inset:0;background:linear-gradient(120deg,#6a7a4e 0%,#b59a7e 40%,#8c6f5a 70%,#3e4a36 100%)}
.hero-search{position:absolute;left:460px;top:245px;width:280px;height:36px;background:#fff;border-radius:3px;display:flex;align-items:center;justify-content:space-between;padding:0 12px;color:#999;font-size:12px}
.hero-title{position:absolute;top:295px;width:100%;text-align:center;color:#fff;font-size:20px}
.hero-cta{position:absolute;left:550px;top:335px;padding:8px 22px}

.welcome{position:absolute;left:260px;top:512px;width:680px;height:308px;background:#fff;box-shadow:0 4px 16px rgba(0,0,0,.15);text-align:center;padding:30px 50px;z-index:2}
.welcome h1{font-size:30px;color:var(--red);margin-bottom:4px}
.welcome h1 span{color:var(--ink)}
.rule{width:60px;height:3px;background:var(--red);margin:8px auto 16px}
.welcome p{font-size:12px;color:var(--muted);margin-bottom:12px}

/* students */
.students{top:840px;height:420px}
.students .photo{left:0;top:0;width:590px;height:420px;background:linear-gradient(135deg,#d9c8a8,#8fa3b5 50%,#c9b089)}
.students-body{position:absolute;left:620px;top:20px;width:540px}
.section-title{font-size:30px;color:var(--ink)}
.section-title.light{color:#fff}
.students-body .rule{margin:6px 0 14px}
.lead{font-size:12px;color:var(--muted)}
.feature{display:flex;gap:18px;margin-top:22px;align-items:flex-start}
.diamond{width:34px;height:34px;flex:none;margin:6px}
.feature h3{font-size:15px;color:var(--ink)}
.feature p{font-size:12px;color:var(--muted)}

/* courses */
.courses{top:1260px;height:500px;background:linear-gradient(var(--red),var(--red-dark));text-align:center;color:#fff}
.courses .section-title{padding-top:36px}
.courses .rule{background:#fff}
.courses .lead{color:#f2cfd1;width:700px;margin:0 auto}
.course-row{position:absolute;left:230px;top:170px;display:flex;gap:12px}
.course{width:176px;height:300px;background:#fff;color:var(--ink);text-align:left;position:relative}
.course .photo{position:static;height:130px;background:linear-gradient(135deg,#a89580,#6e7f91)}
.price{position:absolute;left:64px;top:108px;width:48px;height:48px;border-radius:50%;background:var(--red);color:#fff;font-weight:700;font-size:14px;display:flex;align-items:center;justify-content:center;border:3px solid #fff}
.course h4{font-size:12px;color:var(--red);padding:34px 12px 6px}
.course p{font-size:11px;color:var(--muted);padding:0 12px}
.course .meta{position:absolute;bottom:0;left:0;right:0;border-top:1px solid var(--line);padding:8px 12px;font-size:10px;color:var(--muted)}
.arrow{position:absolute;top:300px;width:30px;height:30px}

/* schools */
.schools{top:1760px;height:440px}
.schools-body{position:absolute;left:60px;top:24px;width:540px}
.schools-body .rule{margin:6px 0 14px}
.schools-body p{font-size:12px;color:var(--muted);margin-bottom:14px}
.schools-body b{color:var(--red);text-transform:uppercase;font-size:11px}
.schools .photo{left:640px;top:0;width:560px;height:440px;background:linear-gradient(160deg,#a9b79a,#7d5d58 50%,#3f4b5e)}

/* news */
.news{top:2200px;height:600px}
.news .photo{inset:0;background:linear-gradient(90deg,#7b6a5a 0%,#b6b2a3 33%,#6d8a5f 66%,#8d7c6c 100%)}
.news-panel{position:absolute;left:400px;top:70px;width:520px;height:500px;background:var(--red);color:#fff;padding:26px 28px}
.news-panel .section-title{color:#fff;font-size:26px}
.news-panel .rule{background:#fff;margin:6px 0 10px}
.news-panel .lead{color:#f2cfd1}
.news-item{display:flex;gap:12px;margin-top:18px;background:#fff;color:var(--ink);height:100px}
.news-item .photo{position:static;width:150px;background:linear-gradient(135deg,#a38f7c,#6f8197)}
.news-date{width:70px;text-align:center;padding-top:16px;color:var(--red)}
.news-date strong{display:block;font-size:32px;line-height:1;font-family:"Roboto Condensed",sans-serif}
.news-date span{font-size:10px;color:var(--muted)}
.news-text{padding:12px 12px 0 0;font-size:11px;color:var(--muted);flex:1}
.news-text h4{font-size:12px;color:var(--ink);margin-bottom:3px}

/* teachers */
.teachers{top:2800px;height:540px;background:var(--mist);text-align:center}
.teachers .section-title{padding-top:34px}
.teachers .lead{width:660px;margin:0 auto}
.teacher{position:absolute;border-radius:50%;background:linear-gradient(#c9c9c9,#8f8f8f);border:4px solid #fff}
.teacher.lead-card{left:488px;top:130px;width:224px;height:224px;background:linear-gradient(#bfc6cf,#6d7a88)}
.teacher-name{position:absolute;top:368px;width:100%;font-size:14px;color:var(--red)}
.teacher-role{position:absolute;top:390px;width:100%;font-size:11px;color:var(--muted)}
.teacher-links{position:absolute;top:420px;left:564px;display:flex;gap:12px}

/* subscribe */
.subscribe{top:3340px;height:160px;background:linear-gradient(var(--red),var(--red-dark));text-align:center;color:#fff}
.subscribe .section-title{color:#fff;padding-top:22px;font-size:26px}
.subscribe .lead{color:#f2cfd1;width:640px;margin:4px auto 14px;font-size:11px}
.subscribe-form{display:flex;justify-content:center}
.subscribe-form span:first-child{width:340px;height:34px;background:#fff;color:#999;text-align:left;padding:8px 12px;font-size:12px}
.subscribe-form .btn{background:var(--footer);border-radius:0;padding:9px 20px}

/* footer */
.site-footer{top:3500px;height:320px;background:var(--footer);color:#bbb}
.social{position:absolute;top:18px;left:540px;display:flex;gap:14px}
.footer-cols{position:absolute;top:90px;left:60px;display:flex;gap:60px}
.footer-col{width:225px;font-size:11px}
.footer-col h5{font-size:14px;color:#fff;margin-bottom:12px}
.footer-col li{list-style:none;padding:4px 0;border-bottom:1px solid #3a3a3a}
.footer-bar{top:3820px;height:32px;background:var(--footer-deep);color:#999;font-size:11px;padding:8px 60px}
</style>
</head>
<body>

<header class="block site-header">
  <div class="brand"><span class="brand-mark"></span><span class="brand-name">The Brightpath Scholar</span></div>
  <div class="contact-strip">Call us: <b>(555) 010-0147</b></div>
  <nav class="main-nav"><a>Home</a><a>About</a><a>Schools</a><a>Students</a><a>Member Area</a><a>News</a><a>Contact</a></nav>
  <span class="btn login">Login / Register</span>
</header>

<section class="block hero">
  <div class="photo" role="img" aria-label="Smiling group of college students outdoors on campus"></div>
  <div class="hero-search"><span>Search</span>
    <svg width="14" height="14" viewBox="0 0 14 14"><circle cx="6" cy="6" r="4.5" fill="none" stroke="#999" stroke-width="1.6"/><line x1="9.5" y1="9.5" x2="13" y2="13" stroke="#999" stroke-width="1.6"/></svg></div>
  <h2 class="heading hero-title">We have the largest collection of courses</h2>
  <span class="btn hero-cta">View All Courses</span>
</section>

<section class="welcome">
  <h1 class="heading"><span>Welcome</span> The Brightpath Scholar</h1>
  <div class="rule"></div>
  <p>Our online college fair brings non-traditional students, homeschoolers and adult learners together with admissions officers and advisors, all in one friendly place you can visit anytime.</p>
  <p>Browse school booths, ask questions, compare programs and plan your next step without travel or long waits. Every booth links to a detail page where schools share their offers, deadlines and support for learners like you.</p>
  <span class="btn">Read More</span>
</section>

<section class="block students">
  <div class="photo" role="img" aria-label="Students studying together around a table"></div>
  <div class="students-body">
    <h2 class="heading section-title">Students</h2>
    <div class="rule"></div>
    <p class="lead">Meet colleges that welcome your path. Register as a member to save booths, message advisors and reach the members only area.</p>
    <div class="feature">
      <svg class="diamond" viewBox="0 0 34 34"><rect x="7" y="7" width="20" height="20" transform="rotate(45 17 17)" fill="none" stroke="#b3121b" stroke-width="2"/><circle cx="17" cy="17" r="3" fill="#b3121b"/></svg>
      <div><h3 class="heading">Library System</h3><p>Guides, checklists and sample essays for every step of your application.</p></div>
    </div>
    <div class="feature">
      <svg class="diamond" viewBox="0 0 34 34"><rect x="7" y="7" width="20" height="20" transform="rotate(45 17 17)" fill="none" stroke="#b3121b" stroke-width="2"/><circle cx="17" cy="17" r="3" fill="#b3121b"/></svg>
      <div><h3 class="heading">Online Class</h3><p>Live sessions with admissions officers on aid, credits and transcripts.</p></div>
    </div>
    <div class="feature">
      <svg class="diamond" viewBox="0 0 34 34"><rect x="7" y="7" width="20" height="20" transform="rotate(45 17 17)" fill="none" stroke="#b3121b" stroke-width="2"/><circle cx="17" cy="17" r="3" fill="#b3121b"/></svg>
      <div><h3 class="heading">Online Course</h3><p>Short self-paced courses to prepare for testing and college study.</p></div>
    </div>
  </div>
</section>

<section class="block courses">
  <h2 class="heading section-title light">Popular Courses</h2>
  <div class="rule"></div>
  <p class="lead">Explore the courses our members enjoy most, taught by partner schools and open to learners at any stage of life.</p>
  <svg class="arrow" style="left:190px" viewBox="0 0 30 30"><path d="M19 6 L10 15 L19 24" fill="none" stroke="#fff" stroke-width="3"/></svg>
  <div class="course-row">
    <article class="course"><div class="photo" role="img" aria-label="Students in a lab class"></div><span class="price">$60</span><h4 class="heading">Power Electronics</h4><p>Circuits, converters and hands-on project work.</p><div class="meta">12 Lessons · 4 Weeks</div></article>
    <article class="course"><div class="photo" role="img" aria-label="Student writing at a desk"></div><span class="price">$40</span><h4 class="heading">Introduction to Calculus</h4><p>Limits, derivatives and the basics of integrals.</p><div class="meta">10 Lessons · 5 Weeks</div></article>
    <article class="course"><div class="photo" role="img" aria-label="Classroom with students raising hands"></div><span class="price">$70</span><h4 class="heading">Time Management Course</h4><p>Plan study time around work and family life.</p><div class="meta">8 Lessons · 3 Weeks</div></article>
    <article class="course"><div class="photo" role="img" aria-label="Group of students in a lecture hall"></div><span class="price">$50</span><h4 class="heading">College Writing</h4><p>Build clear essays for classes and applications.</p><div class="meta">9 Lessons · 4 Weeks</div></article>
  </div>
  <svg class="arrow" style="left:980px" viewBox="0 0 30 30"><path d="M11 6 L20 15 L11 24" fill="none" stroke="#fff" stroke-width="3"/></svg>
</section>

<section class="block schools">
  <div class="schools-body">
    <h2 class="heading section-title">Schools</h2>
    <div class="rule"></div>
    <p>Every school on the fair has its own virtual booth. Step inside to see programs, admission rules and the people ready to answer your questions.</p>
    <p><b>For students, free membership</b> gives you a saved list of booths, direct messages with advisors and early notice of live events hosted by colleges near you or online.</p>
    <p><b>For colleges and universities,</b> a booth puts your programs in front of motivated homeschoolers and adult learners, with tools to share dates, aid details and open days.</p>
    <p><b>For independent college advising,</b> our advisor pages help you meet families looking for guidance and share your services with a growing community.</p>
  </div>
  <div class="photo" role="img" aria-label="Students walking together on a college campus"></div>
</section>

<section class="block news">
  <div class="photo" role="img" aria-label="Smiling students holding books, shown at the sides of the section"></div>
  <div class="news-panel">
    <h2 class="heading section-title">News</h2>
    <div class="rule"></div>
    <p class="lead">Fresh tips and stories for students planning college on their own terms.</p>
    <div class="news-item"><div class="news-date"><strong>01</strong><span>MAY 2017</span></div><div class="photo" role="img" aria-label="Students in a classroom"></div><div class="news-text"><h4>Three College Costs You Forget to Plan For</h4>Books, fees and travel can add up fast.</div></div>
    <div class="news-item"><div class="news-date"><strong>25</strong><span>MAY 2017</span></div><div class="photo" role="img" aria-label="Graduates in caps and gowns"></div><div class="news-text"><h4>Why Tuition Keeps Rising Each Year</h4>A plain look at what drives the price.</div></div>
    <div class="news-item"><div class="news-date"><strong>04</strong><span>MAY 2017</span></div><div class="photo" role="img" aria-label="Students working on laptops"></div><div class="news-text"><h4>City Schools Face New Budget Choices</h4>What local changes mean for students.</div></div>
  </div>
</section>

<section class="block teachers">
  <h2 class="heading section-title">Meet Our Teachers</h2>
  <div class="rule"></div>
  <p class="lead">Friendly experts and advisors who know the path of non-traditional learners and love helping them succeed.</p>
  <div class="teacher" style="left:250px;top:190px;width:90px;height:90px" role="img" aria-label="Teacher portrait"></div>
  <div class="teacher" style="left:360px;top:175px;width:110px;height:110px" role="img" aria-label="Teacher portrait"></div>
  <div class="teacher lead-card" role="img" aria-label="Featured teacher portrait"></div>
  <div class="teacher" style="left:730px;top:175px;width:110px;height:110px" role="img" aria-label="Teacher portrait"></div>
  <div class="teacher" style="left:860px;top:190px;width:90px;height:90px" role="img" aria-label="Teacher portrait"></div>
  <div class="heading teacher-name">Daniel Mercer</div>
  <div class="teacher-role">College Advisor</div>
  <div class="teacher-links">
    <svg width="22" height="22" viewBox="0 0 22 22"><rect x="4" y="4" width="14" height="14" transform="rotate(45 11 11)" fill="#b3121b"/></svg>
    <svg width="22" height="22" viewBox="0 0 22 22"><rect x="4" y="4" width="14" height="14" transform="rotate(45 11 11)" fill="#b3121b"/></svg>
    <svg width="22" height="22" viewBox="0 0 22 22"><rect x="4" y="4" width="14" height="14" transform="rotate(45 11 11)" fill="#b3121b"/></svg>
  </div>
</section>

<section class="block subscribe">
  <h2 class="heading section-title">Subscribed Members</h2>
  <p class="lead">Join free to save school booths, talk with advisors and enter the members only area.</p>
  <div class="subscribe-form"><span>Your Email</span><span class="btn">Subscribe</span></div>
</section>

<footer class="block site-footer">
  <div class="social">
    <svg width="30" height="30" viewBox="0 0 30 30"><rect x="6" y="6" width="18" height="18" transform="rotate(45 15 15)" fill="#b3121b"/></svg>
    <svg width="30" height="30" viewBox="0 0 30 30"><rect x="6" y="6" width="18" height="18" transform="rotate(45 15 15)" fill="#b3121b"/></svg>
    <svg width="30" height="30" viewBox="0 0 30 30"><rect x="6" y="6" width="18" height="18" transform="rotate(45 15 15)" fill="#b3121b"/></svg>
    <svg width="30" height="30" viewBox="0 0 30 30"><rect x="6" y="6" width="18" height="18" transform="rotate(45 15 15)" fill="#b3121b"/></svg>
  </div>
  <div class="footer-cols">
    <div class="footer-col"><h5 class="heading">About Us</h5><p>An online college fair where non-traditional students meet schools and advisors. Browse booths, join live events and plan your next step from home.</p></div>
    <div class="footer-col"><h5 class="heading">Popular Courses</h5><ul><li>Power Electronics</li><li>Introduction to Calculus</li><li>Time Management</li><li>College Writing</li></ul></div>
    <div class="footer-col"><h5 class="heading">Quick Links</h5><ul><li>Schools</li><li>Students</li><li>Member Area</li><li>Contact</li></ul></div>
    <div class="footer-col"><h5 class="heading">Contact Us</h5><ul><li>Phone: (555) 010-0147</li><li>hello@brightpathscholar.example</li><li>brightpathscholar.example</li></ul></div>
  </div>
</footer>
<div class="block footer-bar">© Copyright 2017 The Brightpath Scholar. All Rights Reserved.</div>

</body>
</html>
```